Crestline Gas and Plumbing Business Card Design

I am after a business card design for my plumbing business called 'Crestline Gas & Plumbing'. I do all types of plumbing and gas work and specialise in general maintenance plumbing. Would like to see designs using current logo

Industry/Entity Type

Plumbing

Contact Information for Business Card

Name - Dale Whitcombe
Phone number - 0455163027
Email - admin@crestlinegasandplumbing.example.com.au
ABN - 68204915336

```html
<!DOCTYPE html>
<html lang="en">
<head>
<meta charset="UTF-8">
<title>Crestline Gas &amp; Plumbing – Business Card</title>
<link rel="stylesheet" href="https://fonts.googleapis.com/css2?family=Montserrat:wght@400;500;700;800&display=swap">
<style>
  :root {
    --stage: #d4d8d9;
    --paper: #f3f3f1;
    --navy: #221f8f;
    --navy-logo: #1f4fa8;
    --orange: #e07d1c;
    --ink: #3b3b3b;
    --white: #ffffff;
  }
  * { box-sizing: border-box; margin: 0; padding: 0; }
  html, body {
    width: 1200px; height: 1050px; overflow: hidden;
    background: var(--stage);
    font-family: "Montserrat", sans-serif;
  }
  .sheet {
    width: 1200px; height: 1050px;
    display: flex; flex-direction: column;
    align-items: center; justify-content: center; gap: 60px;
  }
  .card {
    position: relative;
    width: 760px; height: 434px;
    box-shadow: 0 18px 40px rgba(40, 50, 60, 0.22);
  }
  .card__frame {
    position: absolute; inset: 28px;
    border: 2px solid var(--navy);
  }
  /* Front */
  .card--front { background: var(--paper); }
  .front__layout {
    position: absolute; inset: 0;
    display: flex; align-items: center;
    padding: 0 60px 0 70px;
  }
  .brand {
    width: 270px;
    color: var(--navy-logo);
    font-weight: 800; font-size: 30px; line-height: 1.12;
    text-transform: uppercase; letter-spacing: 0.5px;
  }
  .divider {
    width: 2px; height: 190px;
    background: var(--orange);
    margin: 0 30px 0 20px;
  }
  .contact__name {
    color: var(--orange);
    font-weight: 700; font-size: 23px;
    margin-bottom: 18px;
  }
  .contact__list { list-style: none; }
  .contact__item {
    display: flex; align-items: center; gap: 10px;
    color: var(--ink); font-size: 15px; font-weight: 500;
    margin-bottom: 9px;
    white-space: nowrap;
  }
  .contact__icon {
    flex: none; width: 20px; height: 20px;
  }
  /* Back */
  .card--back { background: var(--navy); }
  .card--back .card__frame { border-color: var(--white); }
  .back__brand {
    position: absolute; inset: 0;
    display: flex; flex-direction: column;
    align-items: center; justify-content: center;
    color: var(--white);
    font-weight: 800; font-size: 46px; line-height: 1.1;
    text-transform: uppercase; letter-spacing: 1px; text-align: center;
  }
</style>
</head>
<body>
<main class="sheet">

  <section class="card card--front" aria-label="Business card front">
    <div class="card__frame"></div>
    <div class="front__layout">
      <div class="brand">Crestline<br>Gas &amp; Plumbing</div>
      <div class="divider"></div>
      <div class="contact">
        <p class="contact__name">Dale Whitcombe</p>
        <ul class="contact__list">
          <li class="contact__item">
            <svg class="contact__icon" viewBox="0 0 20 20" aria-hidden="true">
              <circle cx="10" cy="10" r="10" fill="#e07d1c"/>
              <path d="M7 5.5l1.8 2.2-1 1.2c.7 1.4 1.8 2.5 3.2 3.2l1.2-1 2.2 1.8-1 1.6c-3.6-.3-7-3.7-7.3-7.3z" fill="#fff"/>
            </svg>
            0455163027
          </li>
          <li class="contact__item">
            <svg class="contact__icon" viewBox="0 0 20 20" aria-hidden="true">
              <circle cx="10" cy="10" r="10" fill="#e07d1c"/>
              <rect x="5" y="6.5" width="10" height="7" rx="1" fill="none" stroke="#fff" stroke-width="1.3"/>
              <path d="M7 9h3M7 11h5" stroke="#fff" stroke-width="1.2"/>
            </svg>
            ABN - 68204915336
          </li>
          <li class="contact__item">
            <svg class="contact__icon" viewBox="0 0 20 20" aria-hidden="true">
              <circle cx="10" cy="10" r="10" fill="#e07d1c"/>
              <rect x="5" y="6.5" width="10" height="7" fill="#fff"/>
              <path d="M5 6.5l5 4 5-4" fill="none" stroke="#e07d1c" stroke-width="1.1"/>
            </svg>
            admin@crestlinegasandplumbing.example.com.au
          </li>
          <li class="contact__item">
            <svg class="contact__icon" viewBox="0 0 20 20" aria-hidden="true">
              <circle cx="10" cy="10" r="10" fill="#e07d1c"/>
              <circle cx="10" cy="10" r="5" fill="none" stroke="#fff" stroke-width="1.2"/>
              <path d="M5 10h10M10 5c-2.5 3-2.5 7 0 10M10 5c2.5 3 2.5 7 0 10" fill="none" stroke="#fff" stroke-width="1"/>
            </svg>
            www.crestlinegasandplumbing.example.com.au
          </li>
        </ul>
      </div>
    </div>
  </section>

  <section class="card card--back" aria-label="Business card back">
    <div class="card__frame"></div>
    <div class="back__brand">Crestline<br>Gas &amp; Plumbing</div>
  </section>

</main>
</body>
</html>
```